2 Creative Website Banners for Furniture Brand

Morning Tobrasca....
The get a great night sleep banner is complete - we are happy with that one.
Ive uploaded a slightly different concept for the other banner below. This is just something rough ive thrown together. But you can see I have added a curve, a maroon coloured background which is slightly transparent and a big heart in the background....
I do not necessarily want to use this heart image but something a bit like this (a nice graphic, gif etc) but something quite elegant faded in, or perhaps a number of hearts (done in a tasteful way). Also can we keep the typography in the same format as you can see for this one.
Nearly there :)!
Industry/Entity Type
Furniture

```html
<!DOCTYPE html>
<html lang="en">
<head>
<meta charset="utf-8">
<title>Calverly Web Banners</title>
<link href="https://fonts.googleapis.com/css2?family=Cinzel:wght@400;500&family=Montserrat:wght@400;500&family=Poppins:wght@300;400&family=Roboto:wght@300&display=swap" rel="stylesheet">
<style>
  :root {
    --board: #3a3a3a;
    --white: #ffffff;
    --strip: #e0d8c8;
    --strip-text: #9a7d45;
    --plum: #3a1f3a;
    --nav: #a39383;
    --gold: #c9a44a;
    --gold-deep: #8f6e1f;
    --silver: #e6e6e6;
    --hero-dark: #1b1819;
    --tile-beige: #bcad97;
    --tile-text: #6f6250;
    --icon-gold: #c9a82e;
    --body-grey: #555;
  }
  * { margin: 0; padding: 0; box-sizing: border-box; }
  html, body { width: 845px; height: 1200px; overflow: hidden; }
  body { background: var(--board); position: relative; font-family: "Montserrat", sans-serif; }

  .sample-label {
    position: absolute; left: 78px;
    font-family: "Poppins", sans-serif; font-weight: 300;
    font-size: 19px; letter-spacing: 6px; color: var(--white);
  }
  .sample-label--one { top: 56px; }
  .sample-label--two { top: 616px; }

  .banner {
    position: absolute; left: 78px; width: 692px; height: 466px;
    background: var(--white); overflow: hidden;
    box-shadow: 0 6px 18px rgba(0,0,0,.35);
  }
  .banner--one { top: 97px; }
  .banner--two { top: 656px; }

  .notice-strip {
    height: 13px; background: var(--strip); color: var(--strip-text);
    font-size: 5.6px; text-align: center; line-height: 13px; letter-spacing: -.1px;
  }

  .site-header { position: relative; height: 56px; }
  .brand-name {
    position: absolute; left: 28px; top: 15px;
    font-family: "Montserrat", sans-serif; font-weight: 400;
    font-size: 18px; letter-spacing: 4px; color: var(--plum);
  }
  .phone {
    position: absolute; right: 31px; top: 5px;
    display: flex; align-items: center; gap: 6px;
    font-family: "Roboto", sans-serif; font-weight: 300; font-size: 14.5px; color: var(--plum);
  }
  .phone-dot { width: 12px; height: 12px; border-radius: 50%; background: #c0283a; }
  .account-links {
    position: absolute; right: 33px; top: 35px;
    display: flex; gap: 10px; font-size: 6px; color: var(--plum);
  }
  .account-links span { display: flex; align-items: center; gap: 3px; }
  .account-links svg { width: 9px; height: 9px; }

  .main-nav { position: relative; height: 23px; background: var(--nav); }
  .main-nav a {
    position: absolute; top: 0; line-height: 23px; transform: translateX(-50%);
    color: var(--white); text-decoration: none; font-size: 8.4px; white-space: nowrap;
  }
  .main-nav a.has-menu::after { content: "⌄"; margin-left: 4px; font-size: 8px; position: relative; top: -2px; }

  .hero { position: relative; height: 208px; }
  .hero-backdrop {
    position: absolute; left: 0; top: 0; width: 357px; height: 208px;
  }
  .banner--one .hero-backdrop {
    background: radial-gradient(ellipse at 45% 35%, #2d2729 0%, #1f1b1c 55%, #151213 100%);
  }
  .banner--two .hero-backdrop {
    background: linear-gradient(120deg, #0e0c0d 0%, #221e20 45%, #1a1718 100%);
  }
  .hero-photo {
    position: absolute; left: 357px; top: 0; width: 335px; height: 208px;
    background: linear-gradient(100deg, #4a3f45 0%, #6e5c63 30%, #8f8488 55%, #5d5a62 75%, #a7a9b0 100%);
  }
  .hero-copy { position: absolute; left: 73px; top: 38px; color: var(--white); }
  .hero-kicker {
    font-family: "Poppins", sans-serif; font-weight: 300;
    font-size: 15.5px; letter-spacing: 6.5px;
  }
  .hero-title {
    font-family: "Cinzel", serif; font-weight: 400;
    font-size: 79px; line-height: 66px; letter-spacing: -1px; margin-top: 2px;
  }
  .banner--one .hero-title {
    background: linear-gradient(180deg, #f3dc8e 0%, var(--gold) 45%, var(--gold-deep) 100%);
    -webkit-background-clip: text; background-clip: text; color: transparent;
  }
  .banner--two .hero-title {
    background: linear-gradient(180deg, #ffffff 0%, var(--silver) 50%, #9a9a9a 100%);
    -webkit-background-clip: text; background-clip: text; color: transparent;
  }
  .hero-text {
    font-family: "Poppins", sans-serif; font-weight: 300;
    font-size: 7.4px; line-height: 10px; margin-top: 10px; width: 200px;
  }
  .hero-rule { width: 31px; height: 1.5px; background: var(--gold); margin-top: 12px; }
  .hero-link {
    display: inline-block; margin-top: 9px; color: var(--gold);
    font-family: "Poppins", sans-serif; font-size: 10px; letter-spacing: 1.5px;
  }
  .hero-button {
    display: inline-block; margin-top: 12px; padding: 2px 8px;
    border: 1px solid var(--white); color: var(--white);
    font-family: "Poppins", sans-serif; font-size: 9.5px;
  }
  .banner--two .hero-copy { top: 38px; left: 75px; }
  .banner--two .hero-title { font-size: 82px; line-height: 64px; }

  .room-tiles { position: absolute; top: 323px; left: 0; width: 692px; }
  .room-tile {
    position: absolute; top: 0; width: 128px; height: 128px;
    display: flex; align-items: flex-end; justify-content: center;
  }
  .room-tile__label {
    color: var(--white); font-family: "Montserrat", sans-serif;
    font-size: 9px; letter-spacing: 3.5px; margin-bottom: 6px;
  }
  .room-tile--intro {
    left: 67px; background: var(--tile-beige);
    flex-direction: column; justify-content: center; align-items: center;
  }
  .room-tile--intro::before {
    content: ""; position: absolute; inset: 3px; border: 1px solid rgba(255,255,255,.75);
  }
  .intro-small { font-family: "Cinzel", serif; font-size: 11px; letter-spacing: 7px; color: var(--tile-text); }
  .intro-big { font-family: "Cinzel", serif; font-size: 22px; letter-spacing: 4px; color: var(--tile-text); line-height: 24px; }
  .room-tile--bedroom { left: 211px; background: linear-gradient(160deg, #e8e6e2 0%, #d9d3c9 50%, #a9998a 100%); }
  .room-tile--living { left: 355px; background: linear-gradient(180deg, #e4e4e2 0%, #6b7480 50%, #b08a63 100%); }
  .room-tile--dining { left: 499px; background: linear-gradient(180deg, #f0f1ef 0%, #ddd5c9 55%, #c9bba8 100%); }
</style>
</head>
<body>

<div class="sample-label sample-label--one">WEB_BANNER_ SAMPLE 1</div>

<section class="banner banner--one">
  <div class="notice-strip">COVID 19 - WE ARE TAKING ORDERS AND DELIVERING AS NORMAL</div>
  <header class="site-header">
    <div class="brand-name">CALVERLY</div>
    <div class="phone"><span class="phone-dot"></span>0300 555 0142</div>
    <div class="account-links">
      <span><svg viewBox="0 0 10 10"><circle cx="5" cy="5" r="4" fill="none" stroke="var(--icon-gold)" stroke-width="1.2"/></svg>TRACK ORDER</span>
      <span><svg viewBox="0 0 10 10"><path d="M5 9 L1 5 A2.2 2.2 0 0 1 5 2.5 A2.2 2.2 0 0 1 9 5 Z" fill="var(--icon-gold)"/></svg>MY WISHLIST</span>
      <span><svg viewBox="0 0 10 10"><rect x="1.5" y="3.5" width="7" height="5.5" fill="none" stroke="var(--icon-gold)"/><path d="M3.5 3.5 V2 A1.5 1.5 0 0 1 6.5 2 V3.5" fill="none" stroke="var(--icon-gold)"/></svg>CART (0)</span>
    </div>
  </header>
  <nav class="main-nav">
    <a style="left:97px">HOME</a>
    <a class="has-menu" style="left:204px">BEDROOM</a>
    <a class="has-menu" style="left:328px">LIVING ROOM</a>
    <a class="has-menu" style="left:460px">DINING ROOM</a>
    <a class="has-menu" style="left:585px">CONTACT</a>
  </nav>
  <div class="hero">
    <div class="hero-backdrop" role="img" aria-label="Dark bedroom backdrop with softly faded heart graphics"></div>
    <div class="hero-photo" role="img" aria-label="Photo of an upholstered bed with mirrored bedside cabinet and lamp"></div>
    <div class="hero-copy">
      <div class="hero-kicker">FIND A LOOK YOU</div>
      <div class="hero-title">LOVE</div>
      <p class="hero-text">Lorem Ipsum is simply dummy text of the printing and typesetting industry.</p>
      <div class="hero-rule"></div>
      <span class="hero-link">SHOP IN BEDROOMS</span>
    </div>
  </div>
  <div class="room-tiles">
    <div class="room-tile room-tile--intro"><span class="intro-small">SHOP BY</span><span class="intro-big">ROOM</span></div>
    <div class="room-tile room-tile--bedroom" role="img" aria-label="Photo of a cream bedroom set"><span class="room-tile__label">BEDROOM</span></div>
    <div class="room-tile room-tile--living" role="img" aria-label="Photo of a grey buttoned sofa"><span class="room-tile__label">LIVING</span></div>
    <div class="room-tile room-tile--dining" role="img" aria-label="Photo of a dining table with chairs"><span class="room-tile__label">DINING</span></div>
  </div>
</section>

<div class="sample-label sample-label--two">WEB_BANNER_ SAMPLE 2</div>

<section class="banner banner--two">
  <div class="notice-strip">COVID 19 - WE ARE TAKING ORDERS AND DELIVERING AS NORMAL</div>
  <header class="site-header">
    <div class="brand-name">CALVERLY</div>
    <div class="phone"><span class="phone-dot"></span>0300 555 0142</div>
    <div class="account-links">
      <span><svg viewBox="0 0 10 10"><circle cx="5" cy="5" r="4" fill="none" stroke="var(--icon-gold)" stroke-width="1.2"/></svg>TRACK ORDER</span>
      <span><svg viewBox="0 0 10 10"><path d="M5 9 L1 5 A2.2 2.2 0 0 1 5 2.5 A2.2 2.2 0 0 1 9 5 Z" fill="var(--icon-gold)"/></svg>MY WISHLIST</span>
      <span><svg viewBox="0 0 10 10"><rect x="1.5" y="3.5" width="7" height="5.5" fill="none" stroke="var(--icon-gold)"/><path d="M3.5 3.5 V2 A1.5 1.5 0 0 1 6.5 2 V3.5" fill="none" stroke="var(--icon-gold)"/></svg>CART (0)</span>
    </div>
  </header>
  <nav class="main-nav">
    <a style="left:97px">HOME</a>
    <a class="has-menu" style="left:204px">BEDROOM</a>
    <a class="has-menu" style="left:328px">LIVING ROOM</a>
    <a class="has-menu" style="left:460px">DINING ROOM</a>
    <a class="has-menu" style="left:585px">CONTACT</a>
  </nav>
  <div class="hero">
    <div class="hero-backdrop" role="img" aria-label="Dark bedroom backdrop with faded diamond pattern and mirror"></div>
    <div class="hero-photo" role="img" aria-label="Photo of an upholstered bed with mirrored bedside cabinet and lamp"></div>
    <div class="hero-copy">
      <div class="hero-kicker">FIND A LOOK YOU</div>
      <div class="hero-title">LOVE</div>
      <p class="hero-text">Lorem Ipsum is simply dummy text of the printing and typesetting industry.</p>
      <span class="hero-button">SHOP IN BEDROOMS</span>
    </div>
  </div>
  <div class="room-tiles">
    <div class="room-tile room-tile--intro"><span class="intro-small">SHOP BY</span><span class="intro-big">ROOM</span></div>
    <div class="room-tile room-tile--bedroom" role="img" aria-label="Photo of a cream bedroom set"><span class="room-tile__label">BEDROOM</span></div>
    <div class="room-tile room-tile--living" role="img" aria-label="Photo of a grey buttoned sofa"><span class="room-tile__label">LIVING</span></div>
    <div class="room-tile room-tile--dining" role="img" aria-label="Photo of a dining table with chairs"><span class="room-tile__label">DINING</span></div>
  </div>
</section>

</body>
</html>
```